Letterhead Design Project

I need a simple, clean and corporate letterhead & follow-on letterhead.
The follow-on letterhead should just have the logo only.
Final File Specs:
Full Bleed Size (starting document size)
213 x 300 mm
2517 x 3544 pixels
* Finished artwork should use the full bleed dimensions for best results.
Document Trim Size (final size after being cut)
210 x 297 mm
2480 x 3508 pixels
* Please be sure to keep all text within the safe margin.
Resolution 300 DPI
Accepted file types:-
Adobe Acrobat 9 Document (*.pdf) (recommended)
Adobe Illustrator CS3 Artwork (*.ai) (recommended)
Adobe Photoshop CS3 Image (*.psd) (recommended)
Bitmap Image (*.bmp)
GIF Image (*.gif)
JPEG Image (*.jpg,*.jpeg)
Microsoft PowerPoint 2010 Document (*.ppt)
Microsoft Publisher 2010 Document (*.pub)
Microsoft Word 2010 Document (*.doc)
PCX Image (*.pcx)
PICT Image (*.pic,*.pict,*.pct)
PNG Image (*.png)
PostScript Document (*.ps)
TIF Image (*.tif,*.tiff)
Windows Enhanced Metafile (*.emf)
Windows Metafile (*.wmf)
Requirements
Must have
- My letterhead must have:-
- Logo
- ACN - 482 617 309
- address - Suite 8, 51 Hartwell Ave, Coogee, NSW 2034
- phone - (02) 8371 5926
- fax - (02) 8352 6149
- email - info@brantorguard.com.au
- web - www.brantorguard.com.au
Follow-on letterhead should have the logo only

```html
<!DOCTYPE html>
<html lang="en">
<head>
<meta charset="utf-8">
<title>Brantor Guard Letterhead Set</title>
<link rel="stylesheet" href="https://fonts.googleapis.com/css2?family=Source+Sans+3:wght@400;700&display=swap">
<style>
  :root {
    --backdrop: #f0f0f0;
    --paper: #ffffff;
    --navy: #14132f;
    --green: #8dc63f;
    --ink: #222230;
  }
  * { margin: 0; padding: 0; box-sizing: border-box; }
  html, body {
    width: 1200px;
    height: 900px;
    overflow: hidden;
    background: var(--backdrop);
    font-family: "Source Sans 3", sans-serif;
  }
  .canvas { position: relative; width: 1200px; height: 900px; }
  .sheet {
    position: absolute;
    top: 55px;
    width: 555px;
    height: 788px;
    background: var(--paper);
    box-shadow: 0 2px 5px rgba(0,0,0,0.22);
    overflow: hidden;
  }
  .sheet--first { left: 30px; }
  .sheet--follow { left: 618px; }

  .brand {
    position: absolute;
    left: 52px;
    top: 52px;
    display: flex;
    align-items: center;
    gap: 10px;
  }
  .brand__square {
    width: 30px;
    height: 30px;
    background: var(--navy);
    border-radius: 5px;
  }
  .brand__name {
    font-size: 34px;
    font-weight: 700;
    color: var(--navy);
    letter-spacing: 0.2px;
    line-height: 1;
  }

  .contact {
    position: absolute;
    left: 0;
    width: 555px;
    top: 686px;
    text-align: center;
    font-size: 10px;
    color: var(--ink);
    line-height: 18px;
  }
  .contact__row { display: flex; justify-content: center; align-items: center; gap: 12px; }
  .contact__item { display: inline-flex; align-items: center; gap: 3px; }
  .contact__icon { width: 9px; height: 9px; fill: var(--green); }
  .contact__label { color: var(--green); }

  .footer-band {
    position: absolute;
    left: 0;
    top: 739px;
    width: 555px;
    height: 31px;
    background: var(--navy);
  }
  .footer-band__web {
    position: absolute;
    left: 0;
    width: 475px;
    top: 0;
    line-height: 31px;
    text-align: center;
    font-size: 10.5px;
    color: var(--green);
  }
  .footer-mark {
    position: absolute;
    left: 466px;
    top: 725px;
    width: 54px;
    height: 54px;
    background: var(--navy);
    border: 3px solid var(--paper);
    border-radius: 8px;
  }
</style>
</head>
<body>
<main class="canvas">

  <section class="sheet sheet--first" aria-label="First page letterhead">
    <header class="brand">
      <span class="brand__square"></span>
      <span class="brand__name">Brantor Guard</span>
    </header>

    <address class="contact" style="font-style:normal">
      <div class="contact__row">
        <span class="contact__item">
          <svg class="contact__icon" viewBox="0 0 10 10" aria-hidden="true"><path d="M5 0.5 L10 5 H8.5 V9.5 H6 V6.5 H4 V9.5 H1.5 V5 H0 Z"/></svg>
          Suite 8, 51 Hartwell Ave, Coogee, NSW 2034
        </span>
      </div>
      <div class="contact__row">
        <span class="contact__item">
          <svg class="contact__icon" viewBox="0 0 10 10" aria-hidden="true"><rect x="0" y="0" width="10" height="10" rx="2"/><path d="M3 2 L4.3 3.6 L3.6 4.4 Q4.6 6 5.8 6.6 L6.6 5.8 L8.2 7 L7.2 8.3 Q3.2 7.4 1.8 3 Z" fill="#fff"/></svg>
          (02) 8371 5926
        </span>
        <span class="contact__item">
          <svg class="contact__icon" viewBox="0 0 10 10" aria-hidden="true"><rect x="2.5" y="0.5" width="5" height="3"/><rect x="0.5" y="3.5" width="9" height="4" rx="1"/><rect x="2.5" y="6.5" width="5" height="3" fill="none" stroke="#8dc63f" stroke-width="1"/></svg>
          (02) 8352 6149
        </span>
        <span class="contact__item">
          <svg class="contact__icon" viewBox="0 0 10 10" aria-hidden="true"><rect x="0" y="2" width="10" height="6.5" rx="1"/><path d="M0.5 2.5 L5 6 L9.5 2.5" fill="none" stroke="#fff" stroke-width="0.8"/></svg>
          info@brantorguard.com.au
        </span>
      </div>
      <div class="contact__row">
        <span><span class="contact__label">ACN</span> - 482 617 309</span>
      </div>
    </address>

    <footer class="footer-band">
      <span class="footer-band__web">www.brantorguard.com.au</span>
    </footer>
    <span class="footer-mark" aria-hidden="true"></span>
  </section>

  <section class="sheet sheet--follow" aria-label="Follow-on page letterhead">
    <header class="brand">
      <span class="brand__square"></span>
      <span class="brand__name">Brantor Guard</span>
    </header>
    <footer class="footer-band"></footer>
    <span class="footer-mark" aria-hidden="true"></span>
  </section>

</main>
</body>
</html>
```